Menu Re-Design for The Marlowbrook a british eatery in spanish holiday resort

Looking for a new design for our breakfast and lunch menu....

I have included some pictures of a few menus I like the feel of File No 1,2,3,4,5..... but am open to any ideas you may have....

The menu is to be double sided consisting of a front design with actual menu on reverse....

I have also included the relevant text files you will require...

We do not have a logo or set colour scheme to follow...

Target Market(s)

Predominantly British holidaymakers in popular Spanish resort....

Requirements
Must have
• Menu to be A3 and double sided, split between either a front page design and menu on reverse, or menu divided between both sides....
• Company Name:- The Marlowbrook
Nice to have
• Fun and Bold design whilst maintaining a feel of quality....
Should not have
• Please avoid the use of any food photography....

```html
<!DOCTYPE html>
<html lang="en">
<head>
<meta charset="utf-8">
<title>The Marlowbrook – Day-time Menu</title>
<link href="https://fonts.googleapis.com/css2?family=Roboto+Slab:wght@300&display=swap" rel="stylesheet">
<style>
  :root {
    --backdrop: #e4e4e4;
    --menu-red: #d93227;
    --menu-red-deep: #cf2d23;
    --ink-light: #ffffff;
    --ink-soft: rgba(255, 255, 255, 0.78);
  }
  * { box-sizing: border-box; margin: 0; padding: 0; }
  html, body {
    width: 1200px;
    height: 800px;
    overflow: hidden;
    background: var(--backdrop);
  }
  .canvas {
    position: relative;
    width: 1200px;
    height: 800px;
  }
  .menu-cover {
    position: absolute;
    left: 330px;
    top: 18px;
    width: 540px;
    height: 764px;
    background: linear-gradient(160deg, var(--menu-red-deep), var(--menu-red));
    color: var(--ink-light);
    font-family: "Roboto Slab", Georgia, serif;
    font-weight: 300;
  }
  .cover-header {
    position: absolute;
    top: 34px;
    left: 36px;
    right: 36px;
    display: flex;
    justify-content: space-between;
    align-items: center;
    font-size: 12px;
    letter-spacing: 0.14em;
    text-transform: uppercase;
    color: var(--ink-soft);
  }
  .header-divider {
    width: 1px;
    height: 22px;
    background: var(--ink-soft);
    transform: rotate(25deg);
  }
  .brand-mark {
    position: absolute;
    left: 50%;
    top: 220px;
    width: 240px;
    height: 240px;
    margin-left: -120px;
  }
  .brand-ring {
    position: absolute;
    inset: 0;
  }
  .brand-name {
    position: absolute;
    inset: 0;
    display: flex;
    flex-direction: column;
    align-items: center;
    justify-content: center;
    text-align: center;
    font-size: 30px;
    line-height: 1.15;
    letter-spacing: 0.02em;
    color: var(--ink-light);
  }
  .cover-tagline {
    position: absolute;
    top: 500px;
    left: 0;
    right: 0;
    text-align: center;
    font-size: 15px;
    letter-spacing: 0.12em;
    text-transform: uppercase;
    color: var(--ink-soft);
  }
  .tagline-accent {
    color: var(--ink-light);
    border-bottom: 1px solid var(--ink-light);
    padding-bottom: 2px;
  }
</style>
</head>
<body>
  <main class="canvas">
    <article class="menu-cover">
      <header class="cover-header">
        <span class="header-item">The Marlowbrook</span>
        <span class="header-divider" aria-hidden="true"></span>
        <span class="header-item">Day-time menu</span>
        <span class="header-divider" aria-hidden="true"></span>
        <span class="header-item">Served until 5pm</span>
      </header>

      <div class="brand-mark">
        <svg class="brand-ring" viewBox="0 0 240 240" aria-hidden="true">
          <circle cx="120" cy="120" r="118" fill="none" stroke="#ffffff" stroke-width="1.5"/>
        </svg>
        <h1 class="brand-name"><span>The</span><span>Marlowbrook</span></h1>
      </div>

      <p class="cover-tagline"><span class="tagline-accent">Taste</span> how much we care</p>
    </article>
  </main>
</body>
</html>
```